Report Design Template Needed for Strategy Consulting Co.

I have a small consulting business that does market research, develops marketing strategy, and does business development work (sales, finding partners, preparing for investors) for small and medium-sized companies who can’t afford their own full-time marketing person.

Most of my reports are PowerPoint Decks. There is usually a Title Page, a Table of Contents, an Executive Summary, a Detailed Findings section (with some section breaks, so I need a divider page between sections), and a Recommendations section.

I need a report template/style that is attractive, professional and not too bold such that it takes away from the content, which is what they are paying for.

I have color palette ideas and graphics in the attached brief. Please let me know if you need anything else, or if you need graphic files.

Thank you!!

Target Market(s)

Small business professionals, scientists, business development executives.

Industry/Entity Type

Marketing

Font styles to use
Sans Serif

Requirements
Must have
• Should have the sections listed in the brief. Also, need to be able to import the template complete.
Should not have
• Background must not overtake the text

```html
<!DOCTYPE html>
<html lang="en">
<head>
<meta charset="UTF-8">
<title>Bullet Style Slide</title>
<link href="https://fonts.googleapis.com/css2?family=Oswald:wght@600&family=Source+Sans+3:wght@400;600&display=swap" rel="stylesheet">
<style>
  :root {
    --navy: #143a56;
    --olive: #6d8a2c;
    --canvas: #f2f2f2;
    --body-text: #878787;
    --accent-word: #8f8a4a;
    --placeholder: #d9d9d9;
    --placeholder-text: #1d3d57;
    --rule: #bdbdbd;
    --white: #ffffff;
  }
  * { margin: 0; padding: 0; box-sizing: border-box; }
  html, body { width: 1200px; height: 900px; overflow: hidden; background: var(--canvas); }
  .slide { position: relative; width: 1200px; height: 900px; background: var(--canvas); font-family: "Source Sans 3", sans-serif; }
  .slide-header { position: absolute; left: 0; top: 0; width: 1200px; height: 91px; background: var(--navy); }
  .slide-title { position: absolute; left: 28px; top: 20px; font-family: "Oswald", sans-serif; font-weight: 600; font-size: 37px; line-height: 48px; letter-spacing: 6px; color: var(--white); }
  .header-rule { position: absolute; left: 0; top: 91px; width: 1200px; height: 7px; background: var(--olive); }
  .section-tag { position: absolute; left: 40px; top: 145px; width: 268px; height: 50px; border-radius: 6px; background: var(--olive); color: var(--white); font-weight: 600; font-size: 25px; line-height: 50px; text-align: center; }
  .body-copy { position: absolute; left: 50px; top: 226px; width: 515px; font-size: 20px; line-height: 28px; color: var(--body-text); text-align: justify; }
  .body-copy p { margin-bottom: 28px; }
  .body-copy .highlight { color: var(--accent-word); }
  .image-slot { position: absolute; left: 620px; top: 220px; width: 538px; height: 480px; background: var(--placeholder); display: flex; align-items: center; justify-content: center; }
  .image-slot span { font-size: 50px; color: var(--placeholder-text); letter-spacing: -0.5px; }
  .brand-name { position: absolute; left: 18px; top: 846px; font-weight: 600; font-size: 28px; line-height: 34px; color: var(--navy); }
  .footer-rule { position: absolute; left: 288px; top: 870px; width: 812px; height: 1px; background: var(--rule); }
  .page-number { position: absolute; left: 1108px; top: 850px; width: 50px; height: 40px; background: var(--navy); color: var(--white); font-family: "Oswald", sans-serif; font-weight: 600; font-size: 15px; line-height: 40px; letter-spacing: 1px; text-align: center; }
</style>
</head>
<body>
<main class="slide">
  <header class="slide-header">
    <h1 class="slide-title">BULLET STYLE SLIDE</h1>
  </header>
  <div class="header-rule"></div>

  <div class="section-tag">What we do ?</div>

  <div class="body-copy">
    <p>Lorem Ipsum is simply dummy text of the printing and typesetting industry. Lorem Ipsum has been the industry's standard dummy text ever since the 1500s,</p>
    <p>when an unknown printer took a galley of type and scrambled it to make a type specimen book. Lorem Ipsum is simply dummy text of the printing and typesetting industry. Lorem Ipsum has been the industry's standard dummy text ever since the 1500s, when an unknown printer took a galley of type and scrambled it to make a type specimen book.</p>
    <p>Lorem Ipsum is simply dummy text of the printing and typesetting industry Lorem Ipsum is simply dummy text of the printing and typesetting industry Lorem Ipsum is simply dummy text of the printing and typesetting <span class="highlight">industry</span></p>
  </div>

  <div class="image-slot" role="img" aria-label="Image area for a supporting photo"><span>IMAGE PLACE</span></div>

  <footer>
    <div class="brand-name">Horizon Partners</div>
    <div class="footer-rule"></div>
    <div class="page-number">04</div>
  </footer>
</main>
</body>
</html>
```